Brightwell Amusements Investor Brochure

Start Up Company Brightwell Amusements requires 4 page A4 size brochure outlining and detailing new product. Draft layout attached. Information and points of difference included. Company logo and graphics attached. Final design should sell to investors.

```html
<!DOCTYPE html>
<html lang="en">
<head>
<meta charset="utf-8">
<title>Brightwell Amusements – Investor Brochure Spread</title>
<link href="https://fonts.googleapis.com/css2?family=Raleway:wght@300;400;600;800&family=Roboto:wght@400;500&display=swap" rel="stylesheet">
<style>
  :root{
    --bg:#2b2b2b;
    --paper:#f3f4f5;
    --band:#3a7fc0;
    --band-dark:#2a66a3;
    --navy:#1c3f73;
    --orange:#f29a27;
    --orange-dark:#d9791a;
    --ink:#333a44;
    --muted:#7b8490;
    --grey-band:#dfe1e4;
    --rule:#d5d8dc;
  }
  *{box-sizing:border-box;margin:0;padding:0}
  html,body{width:1200px;height:800px;overflow:hidden;background:var(--bg)}
  body{font-family:"Roboto",Arial,sans-serif;color:var(--ink);position:relative}
  .spread{position:absolute;left:40px;top:30px;width:1120px;height:740px;display:flex}
  .page{position:relative;width:560px;height:740px;background:var(--paper);overflow:hidden}
  .page--left{border-right:1px solid #c9ccd0}
  .header-band{position:absolute;left:0;right:0;top:20px;height:86px;background:linear-gradient(var(--band),var(--band-dark));color:#fff;font-family:"Raleway",sans-serif;text-transform:uppercase}
  .page--left .header-band{text-align:right;padding:14px 22px 0 0}
  .page--right .header-band{text-align:left;padding:14px 0 0 22px}
  .header-band .lead{font-weight:800;font-size:25px;letter-spacing:4px;display:block}
  .header-band .sub{font-weight:300;font-size:31px;letter-spacing:7px;display:block;margin-top:2px}
  .placeholder{position:absolute;border-radius:4px}
  .map-au{left:215px;top:118px;width:210px;height:150px;background:radial-gradient(ellipse at 50% 45%,#5a9ad6,#3b7fc1 70%,transparent 72%)}
  .kiosk{left:40px;top:170px;width:160px;height:380px;background:linear-gradient(160deg,#3b6fb5,#1a3b72 55%,#10264d);border-radius:14px 14px 4px 4px}
  .passenger-table{position:absolute;left:175px;top:280px;width:370px;background:#fff;box-shadow:0 2px 6px rgba(0,0,0,.2)}
  .passenger-table header{background:linear-gradient(var(--band),var(--band-dark));color:#fff;text-align:center;padding:8px 0 7px}
  .passenger-table h2{font-family:"Raleway",sans-serif;font-size:15px;font-weight:400}
  .passenger-table h2 b{font-weight:800}
  .passenger-table header p{font-size:9px;font-style:italic;margin-top:2px}
  table{width:100%;border-collapse:collapse;font-size:8.5px}
  td{height:20px;border-bottom:1px solid var(--rule);padding:0 8px}
  td.city{color:var(--band-dark);text-transform:uppercase;text-align:right;width:28%}
  td.count{color:var(--muted);width:22%}
  td.count.left-col{border-right:1px solid var(--rule)}
  .passenger-table footer{background:var(--orange);color:#fff;text-align:center;font-family:"Raleway",sans-serif;font-size:14px;padding:7px 0}
  .passenger-table footer b{font-weight:800}
  .feature-band{position:absolute;left:0;right:0;bottom:20px;height:130px;background:var(--grey-band);padding:18px 24px 0 30px}
  .feature-list{list-style:none;font-size:11px;color:var(--muted)}
  .feature-list li{position:relative;padding-left:20px;margin-bottom:11px;line-height:1.3}
  .feature-list li::before{content:"";position:absolute;left:0;top:2px;border-left:8px solid var(--band);border-top:5px solid transparent;border-bottom:5px solid transparent}
  .feature-list strong{color:var(--ink)}
  .map-world{left:20px;top:120px;width:520px;height:200px;background:radial-gradient(ellipse at 50% 50%,#4d8fd0,#3a7fc0 65%,transparent 70%)}
  .airport-headline{position:absolute;left:0;right:0;top:340px;text-align:center;font-family:"Raleway",sans-serif;font-weight:800;font-size:12.5px;color:var(--orange-dark)}
  .wifi-chart{position:absolute;left:20px;top:365px;width:520px;height:330px;background:#fff;box-shadow:0 1px 4px rgba(0,0,0,.15)}
  .wifi-chart header{background:linear-gradient(var(--band),var(--band-dark));color:#fff;text-align:center;padding:9px 0 8px}
  .wifi-chart h2{font-family:"Raleway",sans-serif;font-size:14px;font-weight:400;text-transform:uppercase}
  .wifi-chart header p{font-size:8.5px;margin-top:3px}
  .bars{position:absolute;left:0;top:64px;width:100%}
  .bar-row{position:relative;height:28px;display:flex;align-items:center}
  .bar-label{width:150px;text-align:right;font-size:7.5px;color:var(--muted);padding-right:6px}
  .bar{height:11px;background:linear-gradient(var(--orange),var(--orange-dark));box-shadow:2px 2px 2px rgba(0,0,0,.2);min-width:5px}
  .bar-note{font-size:8px;color:var(--ink);margin-left:6px}
</style>
</head>
<body>
<div class="spread">
  <section class="page page--left">
    <div class="header-band"><span class="lead">Coming soon to airports</span><span class="sub">Across Australia</span></div>
    <div class="placeholder map-au" role="img" aria-label="Map of Australia with airport location markers"></div>
    <div class="placeholder kiosk" role="img" aria-label="Brightwell Amusements movie kiosk for travellers"></div>
    <div class="passenger-table">
      <header><h2><b>145,000,000+</b> PASSENGER MOVEMENTS</h2><p>New Airport announced for Western Sydney to cope with increase demand</p></header>
      <table>
        <tr><td class="city">Sydney</td><td class="count left-col">38 437 737</td><td class="city">Melbourne</td><td class="count">30 484 074</td></tr>
        <tr><td class="city">Brisbane</td><td class="count left-col">21 570 625</td><td class="city">Perth</td><td class="count">12 989 955</td></tr>
        <tr><td class="city">Adelaide</td><td class="count left-col">7 460 471</td><td class="city">Gold Coast</td><td class="count">5 789 986</td></tr>
        <tr><td class="city">Cairns</td><td class="count left-col">4 292 485</td><td class="city">Canberra</td><td class="count">2 931 006</td></tr>
        <tr><td class="city">Hobart</td><td class="count left-col">2 098 418</td><td class="city">Darwin</td><td class="count">2 023 665</td></tr>
        <tr><td class="city">Townsville</td><td class="count left-col">1 543 457</td><td class="city">Launceston</td><td class="count">1 267 589</td></tr>
        <tr><td class="city">Williamtown</td><td class="count left-col">1 208 188</td><td class="city">Mackay</td><td class="count">1 083 805</td></tr>
        <tr><td class="city">Sunshine Coast</td><td class="count left-col">891 300</td><td class="city">Karratha</td><td class="count">763 137</td></tr>
        <tr><td class="city">Rockhampton</td><td class="count left-col">694 368</td><td class="city">Alice Springs</td><td class="count">667 383</td></tr>
        <tr><td class="city">Gladstone</td><td class="count left-col">500 429</td><td class="city">Port Hedland</td><td class="count">491 274</td></tr>
      </table>
      <footer>FOR YE FEB 2014. <b>UP 3.1%</b> ON 2013</footer>
    </div>
    <div class="feature-band">
      <ul class="feature-list">
        <li>Current technology allows up to 10,000 encrypted digital movies to be stored on a kiosk.</li>
        <li>Multiple customers can simultaneously browse and rent movies on the Kiosks FREE Wifi.</li>
        <li>Travellers are always killing time waiting to board there flight. Perfect time to browse movies.<br><strong>Target of 1 million transactions in the first 12 months</strong></li>
      </ul>
    </div>
  </section>
  <section class="page page--right">
    <div class="header-band"><span class="lead">Technology built for</span><span class="sub">Global Expansion</span></div>
    <div class="placeholder map-world" role="img" aria-label="World map"></div>
    <p class="airport-headline">TOP 20 AIRPORTS IN THE WORLD EXCEEDED 1.2 BILLION PASSENGERS IN 2013</p>
    <div class="wifi-chart">
      <header><h2>Incorporating blazing fast wifi</h2><p>(Future Devices to Download SD Movies in a few seconds)</p></header>
      <div class="bars">
        <div class="bar-row"><span class="bar-label">WiGig 802.11ad (2015) (7000 Mbps)</span><div class="bar" style="width:255px"></div></div>
        <div class="bar-row"><span class="bar-label">Wifi 802.11ac (1300 Mbps)</span><div class="bar" style="width:47px"></div><span class="bar-note">Orbis Nova S4 &amp; S5</span></div>
        <div class="bar-row"><span class="bar-label">Wifi 802.11n (300 Mbps)</span><div class="bar" style="width:12px"></div><span class="bar-note">2013 Model Lumo Phone/Tab - Download SD Movies in Under 3 Minutes</span></div>
        <div class="bar-row"><span class="bar-label">Wifi 802.11g (108 Mbps)</span><div class="bar" style="width:6px"></div></div>
        <div class="bar-row"><span class="bar-label">FBN 100 (100 Mbps)</span><div class="bar" style="width:6px"></div></div>
        <div class="bar-row"><span class="bar-label">FBN 50 (50 Mbps)</span><div class="bar" style="width:5px"></div></div>
        <div class="bar-row"><span class="bar-label">FBN 25 (25Mbps)</span><div class="bar" style="width:5px"></div></div>
        <div class="bar-row"><span class="bar-label">FBN 12 (12 Mbps)</span><div class="bar" style="width:5px"></div></div>
        <div class="bar-row"><span class="bar-label">ADSL 2+ (24Mbps)</span><div class="bar" style="width:5px"></div></div>
      </div>
    </div>
  </section>
</div>
</body>
</html>
```